indépendant en tant que Massothérapeute et Préparateur Mental, j'ai besoin de ...

Massothérapeute et préparateur mental indépendant, je recherche une carte de visite sobre et dynamique, sans images liées au massage ou à la préparation mentale mais intégrant mon logo. Les couleurs que j'aime bien sont : Blanc, gris, anthracite, noir et jaune

Contact Information for Business Card

carte de préférence Horizontale
neutre qui puisse toucher le deux domaines Massothérapie et préparation mentale

Requirements
Must have
• mon projet doit intégrer au recto:
LOGO
Loïc Vermande
078 315 26 49
info@loicvermande-exemple.ch
et éventuellement www.loicvermande-exemple.ch

et au verso les deux adresses:

Chemin des Ormelets 27B
1400 Yverdon-les-Bains

Rue des Tanneries 9
1700 Fribourg

Should not have
• mon projet ne doit pas contenir d'image en liens avec le massage ni la préparation mentale.

```html
<!DOCTYPE html>
<html lang="fr">
<head>
<meta charset="utf-8">
<title>Loïc Vermande – Carte de visite</title>
<link rel="stylesheet" href="https://fonts.googleapis.com/css2?family=Poppins:wght@300;400;500;600&display=swap">
<style>
  :root {
    --stage: #1b1c1f;
    --anthracite: #2a3038;
    --yellow: #f2ec1b;
    --ink: #1d1f22;
    --white: #ffffff;
    --muted: #c9ced4;
  }
  * { box-sizing: border-box; margin: 0; padding: 0; }
  html, body {
    width: 1200px; height: 800px; overflow: hidden;
    background: var(--stage);
    font-family: "Poppins", sans-serif;
  }
  .stage {
    width: 1200px; height: 800px;
    display: flex; align-items: center; justify-content: center; gap: 40px;
  }
  .card {
    position: relative;
    width: 540px; height: 340px;
    border-radius: 26px;
    overflow: hidden;
  }
  /* ---------- Verso (anthracite) ---------- */
  .card--back { background: var(--anthracite); color: var(--white); }
  .identity {
    position: absolute; left: 0; right: 0;
    display: flex; flex-direction: column; align-items: center;
  }
  .card--back .identity { top: 104px; }
  .identity__name {
    font-weight: 600; font-size: 36px; letter-spacing: 1px;
    text-transform: uppercase; line-height: 1.1;
  }
  .identity__role {
    font-weight: 500; font-size: 10.5px; letter-spacing: 1.6px;
    text-transform: uppercase; margin-top: 6px;
  }
  .address {
    position: absolute; display: flex; align-items: center; gap: 10px;
    font-style: normal; font-weight: 400; font-size: 14px; line-height: 1.45; color: var(--muted);
  }
  .address__rule { width: 1px; height: 34px; background: var(--muted); opacity: .7; }
  .address--yverdon { left: 36px; bottom: 40px; }
  .address--fribourg { right: 36px; bottom: 40px; }
  .icon-pin { width: 14px; height: 18px; flex: none; }

  /* ---------- Recto (jaune) ---------- */
  .card--front { background: var(--yellow); color: var(--ink); }
  .card--front .identity { top: 98px; }
  .contact-rule {
    position: absolute; left: 40px; right: 40px; top: 212px;
    height: 1px; background: var(--ink); opacity: .8;
  }
  .contact-list {
    position: absolute; left: 26px; right: 26px; top: 232px;
    display: flex; justify-content: center; align-items: center; gap: 9px;
    list-style: none; font-size: 10px; font-weight: 400;
  }
  .contact-list__item { display: flex; align-items: center; gap: 4px; white-space: nowrap; }
  .contact-list__sep { width: 1px; height: 11px; background: var(--ink); flex: none; }
  .icon-small { width: 10px; height: 10px; flex: none; }
</style>
</head>
<body>
<main class="stage">

  <section class="card card--front" aria-label="Recto">
    <div class="identity">
      <p class="identity__name">Loïc Vermande</p>
      <p class="identity__role">Massothérapeute / Préparateur mental</p>
    </div>
    <div class="contact-rule"></div>
    <ul class="contact-list">
      <li class="contact-list__item">
        <svg class="icon-small" viewBox="0 0 24 24" aria-hidden="true"><path fill="currentColor" d="M6.6 10.8a15.1 15.1 0 0 0 6.6 6.6l2.2-2.2c.3-.3.7-.4 1-.2 1.1.4 2.3.6 3.6.6.6 0 1 .4 1 1V20c0 .6-.4 1-1 1A17 17 0 0 1 3 4c0-.6.4-1 1-1h3.5c.6 0 1 .4 1 1 0 1.3.2 2.5.6 3.6.1.3 0 .7-.2 1z"/></svg>
        078 315 26 49
      </li>
      <li class="contact-list__sep" aria-hidden="true"></li>
      <li class="contact-list__item">
        <svg class="icon-small" viewBox="0 0 24 24" aria-hidden="true"><path fill="currentColor" d="M2 5h20v14H2z"/><path fill="none" stroke="var(--yellow)" stroke-width="2" d="M2.5 5.5 12 13l9.5-7.5"/></svg>
        info@loicvermande-exemple.ch
      </li>
      <li class="contact-list__sep" aria-hidden="true"></li>
      <li class="contact-list__item">
        <svg class="icon-small" viewBox="0 0 24 24" aria-hidden="true"><g fill="none" stroke="currentColor" stroke-width="2"><circle cx="12" cy="12" r="9.5"/><ellipse cx="12" cy="12" rx="4" ry="9.5"/><path d="M2.5 12h19"/></g></svg>
        www.loicvermande-exemple.ch
      </li>
    </ul>
  </section>

  <section class="card card--back" aria-label="Verso">
    <div class="identity">
      <p class="identity__name">Loïc Vermande</p>
      <p class="identity__role">Massothérapeute / Préparateur mental</p>
    </div>
    <address class="address address--yverdon">
      <svg class="icon-pin" viewBox="0 0 14 18" aria-hidden="true"><path fill="var(--yellow)" d="M7 0a7 7 0 0 0-7 7c0 5 7 11 7 11s7-6 7-11a7 7 0 0 0-7-7zm0 9.8A2.8 2.8 0 1 1 7 4.2a2.8 2.8 0 0 1 0 5.6z"/></svg>
      <span class="address__rule" aria-hidden="true"></span>
      <span>Chemin des Ormelets 27B<br>1400 Yverdon-les-Bains</span>
    </address>
    <address class="address address--fribourg">
      <svg class="icon-pin" viewBox="0 0 14 18" aria-hidden="true"><path fill="var(--yellow)" d="M7 0a7 7 0 0 0-7 7c0 5 7 11 7 11s7-6 7-11a7 7 0 0 0-7-7zm0 9.8A2.8 2.8 0 1 1 7 4.2a2.8 2.8 0 0 1 0 5.6z"/></svg>
      <span class="address__rule" aria-hidden="true"></span>
      <span>Rue des Tanneries 9<br>1700 Fribourg</span>
    </address>
  </section>

</main>
</body>
</html>
```